依頼詳細
不動産物件情報の冊子の表紙デザインです。春号らしいイメージと、簡単には捨てられないインパクトのあるデザインをお願いします。
※参考まで前号(冬号)の表紙を添付いたします
会社WEB:http://meridel-works.jp/
※必ずしも、前号のイメージにとらわれる必要はありません
記載項目
タイトル「物件情報 2020 春号」 会社ロゴ:添付参照 10周年記念タイトル:添付参照
希望イメージ
シンプル 複雑
単色 カラフル
暗い 明るい
日常 高級
遊び心 厳粛
未来的 伝統的
女性的 男性的
希望する色
設定なし
納品ファイル
• 高解像度JPG (.jpg)
• イラストレーター形式 (.ai)
補足説明
四半期に一度発行予定ですので、継続して発行して行きます
■ 選んだ理由

最終選考の4案中、一番投票が多かったです。
春の都会をうまく表現したデザインで、表紙にふさわしいと決定しました

■ 提案者全員のお礼・コメント

ご提案いただいた、多数の皆様、誠にありがとうございます。
また、次号の募集にもご参加いただければ幸いです

```html
<!DOCTYPE html>
<html lang="ja">
<head>
<meta charset="utf-8">
<title>物件情報 2020 春号</title>
<link rel="stylesheet" href="https://fonts.googleapis.com/css2?family=Shippori+Mincho:wght@500;700&family=Noto+Sans+JP:wght@400&family=Cinzel:wght@600&display=swap">
<style>
  :root {
    --sky-top: #cfe3f5;
    --sky-mid: #eaf3fb;
    --sky-low: #7fb2dd;
    --blossom: #f2c9d6;
    --blossom-deep: #e7a9bd;
    --ink: #2b2b33;
    --brand: #3d3d46;
    --gold: #c9a24a;
    --city-top: #5b93cc;
    --city-bottom: #1f4f86;
    --caption: #ffffff;
  }
  * { margin: 0; padding: 0; box-sizing: border-box; }
  html, body { width: 855px; height: 1200px; overflow: hidden; background: #fff; }
  .cover {
    position: relative;
    width: 855px;
    height: 1200px;
    overflow: hidden;
    background: linear-gradient(180deg, var(--sky-top) 0%, var(--sky-mid) 45%, #ffffff 62%, var(--sky-low) 100%);
  }
  .cover-art { position: absolute; }
  .blossoms {
    left: 0; top: 0; width: 855px; height: 720px;
    background:
      radial-gradient(ellipse at 20% 15%, var(--blossom-deep) 0%, rgba(231,169,189,0) 45%),
      radial-gradient(ellipse at 70% 5%, var(--blossom) 0%, rgba(242,201,214,0) 50%),
      radial-gradient(ellipse at 5% 60%, var(--blossom) 0%, rgba(242,201,214,0) 35%),
      radial-gradient(ellipse at 90% 55%, var(--blossom) 0%, rgba(242,201,214,0) 30%);
  }
  .hand {
    left: 560px; top: 0; width: 295px; height: 250px;
    background: radial-gradient(ellipse at 70% 40%, #e8c6ae 0%, rgba(232,198,174,0) 65%);
  }
  .clouds {
    left: 0; top: 560px; width: 855px; height: 420px;
    background: radial-gradient(ellipse at 50% 55%, #ffffff 0%, rgba(255,255,255,0.7) 40%, rgba(255,255,255,0) 75%);
  }
  .cityscape {
    left: 0; top: 945px; width: 855px; height: 255px;
    background: linear-gradient(180deg, var(--city-top) 0%, #9cc3e8 40%, var(--city-bottom) 100%);
  }
  .title-band {
    position: absolute; left: 360px; top: 0; width: 150px; height: 830px;
    background: linear-gradient(180deg, rgba(255,255,255,0.6), rgba(255,255,255,0.15));
  }
  .title {
    position: absolute; left: 368px; top: 110px;
    writing-mode: vertical-rl;
    font-family: "Shippori Mincho", serif;
    font-weight: 700;
    font-size: 134px;
    line-height: 1;
    color: var(--ink);
  }
  .issue {
    position: absolute; left: 392px; top: 672px;
    writing-mode: vertical-rl;
    font-family: "Shippori Mincho", serif;
    font-weight: 500;
    font-size: 62px;
    line-height: 1;
    color: var(--ink);
  }
  .year {
    position: absolute; left: 460px; top: 672px;
    writing-mode: vertical-rl;
    text-orientation: upright;
    font-family: "Shippori Mincho", serif;
    font-weight: 500;
    font-size: 34px;
    letter-spacing: 0.02em;
    line-height: 1;
    color: var(--ink);
  }
  .brand {
    position: absolute; left: 0; top: 825px; width: 855px;
    display: flex; flex-direction: column; align-items: center; gap: 8px;
  }
  .brand-dot { width: 60px; height: 60px; border-radius: 50%; background: var(--gold); }
  .brand-name {
    font-family: "Cinzel", serif;
    font-weight: 600;
    font-size: 32px;
    line-height: 1.2;
    letter-spacing: 0.06em;
    color: var(--brand);
  }
  .anniversary {
    position: absolute; left: 385px; top: 1048px;
    width: 85px; height: 85px; border-radius: 50%;
    background: radial-gradient(circle at 40% 35%, #f1dc9a 0%, var(--gold) 55%, #8f6d22 100%);
  }
  .caption {
    position: absolute; left: 0; top: 1150px; width: 855px;
    text-align: center;
    font-family: "Noto Sans JP", sans-serif;
    font-size: 15px;
    line-height: 1.4;
    letter-spacing: 0.05em;
    color: var(--caption);
    text-shadow: 0 1px 2px rgba(0,0,0,0.35);
  }
</style>
</head>
<body>
  <main class="cover">
    <div class="cover-art clouds" role="img" aria-label="春の青空と白い雲"></div>
    <div class="cover-art blossoms" role="img" aria-label="画面上部に広がる満開の桜の枝"></div>
    <div class="cover-art hand" role="img" aria-label="筆を持ち題字を書く手"></div>
    <div class="cover-art cityscape" role="img" aria-label="青空の下に広がる都会の高層ビル街"></div>

    <div class="title-band"></div>
    <h1 class="title">物件情報</h1>
    <p class="issue">春号</p>
    <p class="year">2020</p>

    <div class="brand">
      <span class="brand-dot"></span>
      <span class="brand-name">Meridel Works</span>
    </div>

    <div class="anniversary" role="img" aria-label="10周年記念マーク"></div>
    <p class="caption">株式会社メリデルワークスは、おかげさまで10周年を迎えました。</p>
  </main>
</body>
</html>
```